logo for a full service car wash and detail center
Briar Glen Suds & Shine ,Car Wash & Detail Center
logo for a full service car wash and detail center - Automotive
Creative Brief
Bright & Fun-filled
Nate Ferrando
General Manager
412 Harbrook blvd Cedar Hollow NC 31872
Nate.briarglensuds@examplemail.com

```html
<!DOCTYPE html>
<html lang="en">
<head>
<meta charset="utf-8">
<title>Briar Glen Suds &amp; Shine – Business Card</title>
<link rel="stylesheet" href="https://fonts.googleapis.com/css2?family=Roboto+Condensed:wght@400;700&display=swap">
<style>
  :root {
    --backdrop: #e6e8ea;
    --card-white: #ffffff;
    --blue-light: #5cc3f0;
    --blue-deep: #1a6fc9;
    --brand-blue: #2a8fd8;
    --text-on-blue: #ffffff;
    --divider: #d4d8dc;
  }
  html, body {
    margin: 0;
    padding: 0;
    width: 1200px;
    height: 908px;
    overflow: hidden;
    background: var(--backdrop);
    font-family: "Roboto Condensed", Arial, sans-serif;
  }
  .card {
    position: absolute;
    left: 100px;
    top: 174px;
    width: 1000px;
    height: 560px;
    border-radius: 36px;
    overflow: hidden;
    display: flex;
    box-shadow: 0 18px 40px rgba(0,0,0,0.18);
  }
  .card-front {
    width: 50%;
    background: var(--card-white);
    display: flex;
    align-items: center;
    justify-content: center;
    border-right: 2px solid var(--divider);
  }
  .brand {
    display: flex;
    align-items: center;
    gap: 18px;
  }
  .brand-dot {
    width: 34px;
    height: 34px;
    border-radius: 50%;
    background: var(--brand-blue);
    flex: none;
  }
  .brand-name {
    color: var(--brand-blue);
    font-weight: 700;
    font-size: 40px;
    line-height: 1.1;
    text-transform: uppercase;
    max-width: 340px;
  }
  .card-back {
    width: 50%;
    background: linear-gradient(120deg, var(--blue-light) 0%, var(--blue-deep) 100%);
    color: var(--text-on-blue);
    padding: 70px 0 0 70px;
    box-sizing: border-box;
  }
  .person-name {
    font-weight: 700;
    font-size: 38px;
    margin: 0;
  }
  .person-title {
    font-weight: 400;
    font-size: 26px;
    margin: 4px 0 48px;
  }
  .address {
    font-size: 22px;
    line-height: 1.4;
    margin: 0 0 16px;
  }
  .contact-line {
    display: flex;
    align-items: center;
    gap: 12px;
    font-size: 22px;
    margin: 8px 0;
  }
  .contact-icon {
    width: 24px;
    height: 24px;
    flex: none;
  }
</style>
</head>
<body>
  <div class="card">
    <section class="card-front">
      <div class="brand">
        <span class="brand-dot"></span>
        <span class="brand-name">Briar Glen Suds &amp; Shine</span>
      </div>
    </section>
    <section class="card-back">
      <h1 class="person-name">Nate Ferrando</h1>
      <p class="person-title">General Manager</p>
      <p class="address">412 Harbrook blvd<br>Cedar Hollow NC 31872</p>
      <div class="contact-line">
        <svg class="contact-icon" viewBox="0 0 24 24" aria-hidden="true">
          <circle cx="12" cy="12" r="11" fill="none" stroke="#fff" stroke-width="1.6"/>
          <path d="M8.5 6.5l2 2-1.2 1.6a7 7 0 0 0 4.6 4.6l1.6-1.2 2 2-1.4 1.6c-4.5 0-9.2-4.7-9.2-9.2z" fill="#fff"/>
        </svg>
        <span>555 201 0147</span>
      </div>
      <div class="contact-line">
        <svg class="contact-icon" viewBox="0 0 24 24" aria-hidden="true">
          <circle cx="12" cy="12" r="11" fill="none" stroke="#fff" stroke-width="1.6"/>
          <rect x="6" y="8" width="12" height="8.5" rx="1" fill="none" stroke="#fff" stroke-width="1.4"/>
          <path d="M6 8.5l6 4.5 6-4.5" fill="none" stroke="#fff" stroke-width="1.4"/>
        </svg>
        <span>Nate.briarglensuds@examplemail.com</span>
      </div>
    </section>
  </div>
</body>
</html>
```